A new home page for Velmora!

Velmora needs a needs a new home page. Something fresh, engaging and encompassing of the services and features of the velmora product.

The product competitors are trandle.example, fobrisquant.example, brixel metrics

Hi there,

I'm on leave until Wednesday, so I'll look at all the designs and post comments.

Thank you!

Reason: Quantity of submissions and I was on business trip.

Target Market(s)

Anyone with a website that wants to track visitors, use live chat, support, 'hello' like bars, etc.

Industry/Entity Type

Zentaro

Font styles to use
Sans Serif

Colors

Designer to choose colors to be used in the design.

Requirements
Must have
• the home page must showcase somehow the product line, which is
Analytics
SEO
Live Chat
Support Tickets
Heat Maps
Plonkit (like waveshelf)

visit velmora.example for a full feature list.

```html
<!DOCTYPE html>
<html lang="en">
<head>
<meta charset="utf-8">
<title>Velmora – Home</title>
<link href="https://fonts.googleapis.com/css2?family=Cabin:wght@400;500;600&family=Francois+One&family=Questrial&display=swap" rel="stylesheet">
<style>
  :root {
    --bar-dark: #262626;
    --ink: #222222;
    --ink-soft: #3a3a3a;
    --nav-ink: #4a4a4a;
    --teal: #4fb6c8;
    --page-bg: #f3f6f8;
    --red: #ea3539;
    --cyan: #2ec4cc;
    --yellow: #fbc02d;
    --white: #ffffff;
    --chat-bg: #2c2d30;
    --chat-ink: #4fb6c8;
  }
  * { box-sizing: border-box; margin: 0; padding: 0; }
  html, body { width: 1200px; height: 1028px; overflow: hidden; }
  body {
    position: relative;
    font-family: "Cabin", sans-serif;
    background: var(--page-bg);
    color: var(--ink);
  }

  .promo-bar {
    position: absolute; left: 0; top: 0; width: 1200px; height: 32px;
    background: var(--bar-dark); color: var(--white);
    font-size: 11.5px; font-weight: 500; letter-spacing: .2px;
    display: flex; align-items: center; justify-content: center;
  }
  .promo-bar a { color: var(--teal); margin-left: 3px; }
  .promo-bar .promo-toggle { position: absolute; left: 975px; top: 7px; }

  .site-header {
    position: absolute; left: 0; top: 32px; width: 1200px; height: 64px;
    background: var(--white);
    box-shadow: 0 2px 3px rgba(0,0,0,.25);
    z-index: 2;
  }
  .brand {
    position: absolute; left: 202px; top: 12px;
    font-family: "Cabin", sans-serif; font-weight: 600;
    font-size: 30px; line-height: 38px; color: var(--ink-soft);
  }
  .main-nav a {
    position: absolute; top: 26px; white-space: nowrap;
    font-size: 10px; letter-spacing: .9px; color: var(--nav-ink);
    text-decoration: none; font-weight: 500;
  }
  .main-nav .login {
    top: 20px; left: 935px; width: 64px; height: 24px;
    background: var(--teal); color: var(--white);
    font-size: 11px; letter-spacing: .4px;
    display: flex; align-items: center; justify-content: center;
    border-radius: 2px;
  }

  .hero {
    position: absolute; left: 0; top: 96px; width: 1200px; height: 476px;
    overflow: hidden;
  }
  .hero-photo {
    position: absolute; inset: 0;
    background:
      radial-gradient(ellipse 260px 190px at 800px 170px, rgba(210,190,200,.55), transparent 70%),
      radial-gradient(ellipse 200px 250px at 860px 330px, rgba(215,165,140,.45), transparent 70%),
      linear-gradient(180deg, #3e3029 0%, #5a463a 45%, #7a6251 75%, #5b4638 100%);
  }
  .hero-copy { position: absolute; left: 198px; top: 92px; width: 380px; color: var(--white); }
  .hero-title {
    font-family: "Francois One", sans-serif; font-weight: 400;
    font-size: 36px; line-height: 42px; white-space: nowrap;
    text-shadow: 0 2px 3px rgba(0,0,0,.4);
  }
  .hero-text { margin-top: 34px; font-size: 13px; line-height: 17.4px; width: 375px; }
  .cta {
    position: absolute; left: 200px; top: 290px; width: 168px; height: 40px;
    background: var(--teal); color: var(--white);
    font-family: "Francois One", sans-serif; font-size: 15px; letter-spacing: .4px;
    display: flex; align-items: center; justify-content: center;
    text-decoration: none; box-shadow: 0 1px 2px rgba(0,0,0,.3);
  }

  .expertise { position: absolute; left: 0; top: 572px; width: 1200px; height: 456px; }
  .section-title {
    position: absolute; top: 44px; width: 100%; text-align: center;
    font-family: "Questrial", sans-serif; font-weight: 400; font-size: 38px; color: var(--ink);
    letter-spacing: -.5px;
  }
  .section-intro {
    position: absolute; top: 98px; left: 220px; width: 760px; text-align: center;
    font-size: 13px; line-height: 17.5px; color: var(--ink);
  }
  .service { position: absolute; top: 205px; width: 200px; text-align: center; }
  .service svg { display: block; margin: 0 auto; }
  .service h3 {
    margin-top: 40px; font-family: "Cabin", sans-serif; font-weight: 500;
    font-size: 18px; color: var(--ink);
  }
  .service p { margin-top: 8px; font-size: 10.4px; line-height: 13.6px; color: var(--ink); }

  .live-chat {
    position: absolute; left: 1054px; top: 720px; width: 52px; height: 158px;
    background: var(--chat-bg); border-radius: 12px 0 0 12px;
  }
  .live-chat-label {
    position: absolute; left: 13px; top: 90px; transform: rotate(-90deg); transform-origin: left top;
    font-family: "Questrial", sans-serif; font-size: 15px; color: var(--chat-ink); white-space: nowrap;
  }
  .live-chat svg { position: absolute; left: 12px; top: 100px; }
</style>
</head>
<body>

<div class="promo-bar">
  Hi, I'm a Plonkit. Get one for your website <a href="#">free!</a>
  <svg class="promo-toggle" width="14" height="18" viewBox="0 0 14 18" aria-hidden="true">
    <path d="M7 0 L14 8 H9.5 V18 H4.5 V8 H0 Z" fill="var(--teal)"/>
  </svg>
</div>

<header class="site-header">
  <div class="brand">Velmora</div>
  <nav class="main-nav">
    <a href="#" style="left:569px">HOME</a>
    <a href="#" style="left:620px">FEATURES</a>
    <a href="#" style="left:694px">PLUGINS</a>
    <a href="#" style="left:759px">WIDGETS</a>
    <a href="#" style="left:831px">FREE SEO TOOLS</a>
    <a href="#" class="login">LOGIN</a>
  </nav>
</header>

<section class="hero">
  <div class="hero-photo" role="img" aria-label="Photo of a conference room presentation, with hands holding a tablet showing a website heat map"></div>
  <div class="hero-copy">
    <h1 class="hero-title">Is Your&nbsp; Website Velmora?</h1>
    <p class="hero-text">Velmora! aims to put all the tools to improve your website's performance in one easy to use place... Velmora! offers the "complete" picture of your website that no other web analytics package offers. Are you Velmora?</p>
  </div>
  <a href="#" class="cta">BECOME A CLIENT</a>
</section>

<section class="expertise">
  <h2 class="section-title">Our Experties</h2>
  <p class="section-intro">Velmora! provides first class web site analytics and seo tools for your website. With Velmora!, easilytrack visitors, monitor sales, see conversion rates, and improve your search strategies</p>

  <div class="service" style="left:221px">
    <svg width="101" height="89" viewBox="0 0 101 89" aria-hidden="true">
      <path d="M8 0 H93 A8 8 0 0 1 101 8 V57 A8 8 0 0 1 93 65 H73 L73 89 L45 65 H8 A8 8 0 0 1 0 57 V8 A8 8 0 0 1 8 0 Z" fill="var(--red)"/>
      <rect x="29" y="17" width="43" height="28" fill="none" stroke="#fff" stroke-width="3"/>
      <rect x="44" y="47" width="13" height="3" fill="#fff"/>
      <rect x="35" y="34" width="4" height="7" fill="#fff"/><rect x="42" y="30" width="4" height="11" fill="#fff"/>
      <rect x="49" y="33" width="4" height="8" fill="#fff"/><rect x="56" y="28" width="4" height="13" fill="#fff"/>
      <rect x="63" y="31" width="4" height="10" fill="#fff"/>
      <polyline points="36,29 43,24 50,27 58,21 65,24" fill="none" stroke="#fff" stroke-width="2"/>
    </svg>
    <h3>Site Analyzer</h3>
    <p>Check your site structure, Links,<br>Popularity &amp; more.</p>
  </div>

  <div class="service" style="left:500px">
    <svg width="101" height="89" viewBox="0 0 101 89" aria-hidden="true">
      <path d="M8 0 H93 A8 8 0 0 1 101 8 V57 A8 8 0 0 1 93 65 H73 L73 89 L45 65 H8 A8 8 0 0 1 0 57 V8 A8 8 0 0 1 8 0 Z" fill="var(--cyan)"/>
      <rect x="28" y="15" width="45" height="36" rx="2" fill="none" stroke="#fff" stroke-width="3"/>
      <line x1="28" y1="22" x2="73" y2="22" stroke="#fff" stroke-width="2"/>
      <circle cx="58" cy="19" r="1.3" fill="#fff"/><circle cx="63" cy="19" r="1.3" fill="#fff"/><circle cx="68" cy="19" r="1.3" fill="#fff"/>
      <circle cx="50.5" cy="46" r="9" fill="#fff"/>
      <circle cx="50.5" cy="46" r="3.5" fill="var(--cyan)"/>
      <g fill="#fff"><rect x="48.5" y="34" width="4" height="5"/><rect x="38" y="44" width="5" height="4"/><rect x="58" y="44" width="5" height="4"/></g>
    </svg>
    <h3>SEO Optimizer</h3>
    <p>Scane and Optimize pages for<br>Optimum results.</p>
  </div>

  <div class="service" style="left:782px">
    <svg width="101" height="89" viewBox="0 0 101 89" aria-hidden="true">
      <path d="M8 0 H93 A8 8 0 0 1 101 8 V57 A8 8 0 0 1 93 65 H73 L73 89 L45 65 H8 A8 8 0 0 1 0 57 V8 A8 8 0 0 1 8 0 Z" fill="var(--yellow)"/>
      <path d="M48 34 L48 13 A21 21 0 1 0 69 34 Z" fill="#fff"/>
      <path d="M53 30 L53 10 A20 20 0 0 1 73 30 Z" fill="#fff"/>
      <path d="M58 25 L58 15 A10 10 0 0 1 68 25 Z" fill="var(--yellow)"/>
    </svg>
    <h3>Live Web Stats</h3>
    <p>Track page views, Links,<br>visiters &amp; keywords.</p>
  </div>
</section>

<aside class="live-chat">
  <span class="live-chat-label">Live Chat</span>
  <svg width="30" height="38" viewBox="0 0 30 38" aria-hidden="true">
    <path d="M15 6 A12 12 0 1 0 24 26 L28 32 L26 22 A12 12 0 0 0 15 6 Z" fill="none" stroke="var(--red)" stroke-width="2.5"/>
    <circle cx="18" cy="20" r="6" fill="var(--red)"/>
  </svg>
</aside>

</body>
</html>
```